Label design for organic saffron, saffron and herbal syrup

We cultivate saffron, Damszen roses, flowers and herbs. We would need a recognizable outfit (label) for our products. Theoretically (and practically) we have "converted" the family coat of arms into a kind of LOGO. I would send this in the attachment. It would be nice if - in one way or another - this LOGO / coat of arms could be used (certainly with other colors). For some time we have played with the idea of changing the second part of the family name "Lindenholm" (in German .... greuth sounds similar to Kraut / herb [English]) .... eg Lindenholm's saffron syrup into the labeling.
Our products are primarily syrups, currently herbal syrup and saffron syrup. Here the first problem arises, the only bottles / caps that are actually approved for syrup filling (hot filling) are appallingly ugly (see attachment), the only possibility of "sprucing up" is to use so-called "shrink sleeves" (here we need a diameter of 31 and a length of about 40), the colors of which are also limited. Besides the syrup, we sell saffron as a spice and various herbal mixtures (see appendix current packaging saffron). Our quantities are small (syrup 200ml-330ml), saffron in the gram range.
We also need quasi the back of the labeling (this should be able to be redefined per charge) .... Batch 1 (with small quantity has eg more of herb xy than the next batch or the saffron syrup with batch xy needs more / less saffron). In addition, we are certified organic (for this reason, the reverse side would also have to contain all the requirements of organic labeling) [see attachment].
We do not really want to address a specific clientele. Maybe just people who want to taste, enjoy, mix drinks, cook .... (and - unfortunately - don't like Vasol syrup :-) and want to pay a bit more, or find our saffron or herbs better than others) .
In summary
- Strong recognition value (possibly inclusion of "coat of arms", color variable ... although I personally don't like yellow that much)
- Saffron syrup (the color of the saffron syrup is yellow / golden-yellow-light orange, in a transparent ugly bottle)
- Herbal syrup (color variable from blue / green / brown / red elements, in transparent ugly bottle)
Saffron and other herbs (very small containers, type of container not yet fixed)
Regarding a potential "style" I can unfortunately give little information. On the one hand, I am in love with minimalism, on the other hand, I find the translucent, cryptic, implied enormously attractive and sometimes even the "overloaded" colorful has its charm. I think that all in all, it just has to be coherent, and then it will be good.
Requirements
Must have
- Integration of Code of Arms, modifiable for different products

```html
<!DOCTYPE html>
<html lang="de">
<head>
<meta charset="utf-8">
<title>Lindenholm Safran-Sirup – Etikett</title>
<link href="https://fonts.googleapis.com/css2?family=Montserrat:wght@500;700&family=Open+Sans:wght@400;700&display=swap" rel="stylesheet">
<style>
  :root {
    --backdrop: #ececec;
    --navy: #221b5c;
    --navy-deep: #1c1650;
    --gold: #c9a646;
    --gold-light: #e6cc7a;
    --gold-dark: #8f7127;
    --paper: #f4f4f6;
    --ink-soft: #cfcbe8;
    --muted: #8d88b5;
  }
  * { box-sizing: border-box; margin: 0; padding: 0; }
  html, body { width: 1200px; height: 1200px; overflow: hidden; background: var(--backdrop); }
  .label {
    position: absolute; left: 255px; top: 47px; width: 690px; height: 1106px;
    background: linear-gradient(180deg, var(--navy) 0%, var(--navy-deep) 100%);
    overflow: hidden; font-family: "Open Sans", sans-serif; color: var(--paper);
  }
  .ornament-band {
    position: absolute; left: 0; top: 0; width: 690px; height: 360px;
    background: radial-gradient(circle at 345px 200px, var(--gold-light) 0%, var(--gold) 35%, var(--gold-dark) 55%, var(--navy) 80%);
    opacity: .85;
  }
  .crest-window {
    position: absolute; left: 0; top: 0; width: 690px; height: 360px;
  }
  .brand {
    position: absolute; left: 0; width: 690px; top: 258px; text-align: center;
    font-family: "Montserrat", sans-serif; font-weight: 500; font-size: 40px;
    color: var(--navy); letter-spacing: 1px;
  }
  .brand-mark {
    position: absolute; left: 315px; top: 110px; width: 60px; height: 60px;
    border-radius: 50%; background: var(--navy);
  }
  .product-band {
    position: absolute; left: 0; top: 360px; width: 690px; height: 67px;
    background: linear-gradient(90deg, var(--gold-dark), var(--gold-light) 35%, var(--gold) 65%, var(--gold-dark));
    display: flex; align-items: center; justify-content: center;
    font-family: "Montserrat", sans-serif; font-weight: 700; font-size: 34px;
    color: var(--paper); letter-spacing: 1px;
    text-shadow: 0 0 2px var(--navy), 0 0 2px var(--navy);
  }
  .mixing {
    position: absolute; left: 0; width: 690px; top: 440px; text-align: center;
    font-family: "Montserrat", sans-serif; font-weight: 500; font-size: 24px; color: var(--ink-soft);
  }
  .crocus {
    position: absolute; left: 166px; top: 520px; width: 340px; height: 580px;
    border-radius: 170px 170px 20px 20px;
    background: linear-gradient(180deg, rgba(201,166,70,.45), rgba(201,166,70,.15));
  }
  .organic-badge {
    position: absolute; left: 193px; top: 900px; width: 87px; height: 166px;
    background: #8fbf6a;
  }
  .volume {
    position: absolute; left: 420px; top: 1046px; font-family: "Montserrat", sans-serif;
    font-size: 20px; font-weight: 500; color: var(--paper);
  }
  .side-text {
    position: absolute; writing-mode: vertical-rl; transform: rotate(180deg);
    font-size: 13px; line-height: 19px;
  }
  .ingredients { left: 28px; top: 450px; height: 640px; width: 76px; color: var(--ink-soft); }
  .ingredients strong { color: var(--paper); }
  .organic-note { left: 588px; top: 450px; height: 420px; color: var(--muted); font-size: 12px; }
  .maker { left: 612px; top: 450px; height: 420px; width: 44px; color: var(--paper); font-weight: 700; font-size: 12.5px; }
  .best-before {
    position: absolute; left: 587px; top: 886px; width: 83px; height: 194px;
    border: 2px solid var(--paper); display: flex;
  }
  .best-before span {
    writing-mode: vertical-rl; transform: rotate(180deg); font-weight: 700; font-size: 14px;
    padding: 6px 4px; text-align: right;
  }
  .best-before .date-field { flex: 1; background: #ffffff; }
</style>
</head>
<body>
  <section class="label">
    <div class="ornament-band" role="img" aria-label="Goldenes Mandala-Ornament auf Marineblau"></div>
    <svg class="crest-window" viewBox="0 0 690 360" width="690" height="360">
      <circle cx="345" cy="205" r="190" fill="none" stroke="var(--gold-light)" stroke-width="8"/>
      <rect x="300" y="0" width="90" height="120" fill="var(--paper)"/>
      <circle cx="345" cy="205" r="180" fill="var(--paper)"/>
      <rect x="0" y="340" width="690" height="20" fill="var(--gold)"/>
    </svg>
    <div class="brand-mark"></div>
    <div class="brand">Lindenholm</div>

    <div class="product-band">SAFRAN - SIRUP</div>
    <div class="mixing">Mixing ratio 1:7</div>

    <div class="crocus" role="img" aria-label="Goldene Strichzeichnung einer Krokusblüte"></div>
    <div class="organic-badge" role="img" aria-label="Bio-Zertifizierungszeichen"></div>
    <div class="volume">300mL</div>

    <p class="side-text ingredients"><strong>ZUTATEN:</strong> Wasser, Rohrzucker*, Zitronensaft*, Safran* (0,2 %). Nach dem Öffnen kühl lagern und innerhalb von vier Wochen verbrauchen. Vor Gebrauch gut schütteln. Mit Wasser, Soda oder Sekt mischen. Ideal für Cocktails, Desserts und Tee. Charge siehe Flaschenboden.</p>
    <p class="side-text organic-note">*aus kontrolliert biologischer Landwirtschaft</p>
    <p class="side-text maker">Expertly crafted by: Marbach-Lindenholm<br>1234 Street Name, Any City, District, Country</p>

    <div class="best-before">
      <span>Best Before:</span>
      <div class="date-field"></div>
    </div>
  </section>
</body>
</html>
```